Symposium Flyer

I need a flyer for advertising an upcoming symposium titled, "Stirring and settling the chromatin map", I am organizing as well as a webpage design for the symposium. The Symposium is taking place on Thursday, February 7th, 2019 at the Halvorsen College Dunmere School of Medicine. It is being held by the Genomic Regulation Collegium at the Vantreck Hall for Applied Discovery (Kellaway Auditorium and Lobby, 2750 Orchard Terrace Way, Philadelphia, PA 19187). You can view previous symposiums from our institution at https://events.hdsm-example.org/genreg/meetings/

Our Keynote speakers for this symposium are:
Ottokar Brummell, M.D., Professor of Biology at the Northvale Polytechnic of Applied Science; Founding Member of the Corriveau Foundation for Life Science Study; Member of the Council of Clinical Scholars.
AND
Thomas (Tom) Weylund, M.D., President of the Lumavex Centers for Therapeutic Discovery (LCTD)

We will be adding 8 more speakers to this event, so please leave room for extra speakers to be added and for a website registration link and QR code to be added.

Please email me should have additional questions - corvi@hdsm-example.org

```html
<!DOCTYPE html>
<html lang="en">
<head>
<meta charset="utf-8">
<title>Stirring and Settling the Chromatin Map – Symposium Flyer</title>
<link rel="stylesheet" href="https://fonts.googleapis.com/css2?family=Anton&family=Arimo:wght@400;700&display=swap">
<style>
:root{
  --page:#e9e6e1;
  --white:#ffffff;
  --red:#d12836;
  --blue:#1b4d94;
  --blue-deep:#0f3474;
  --title-blue:#1c4f98;
  --photo-a:#f1ede6;
  --photo-b:#cfc6b6;
}
*{box-sizing:border-box;margin:0;padding:0}
html,body{width:1200px;height:1200px;overflow:hidden;background:var(--page)}
body{font-family:"Arimo",Arial,sans-serif;position:relative}
.flyer{
  position:absolute;left:195px;top:45px;width:1013px;height:1388px;
  transform:scale(.8);transform-origin:0 0;overflow:hidden;background:var(--white);
  box-shadow:0 4px 18px rgba(0,0,0,.18);
}
.flyer__bg{position:absolute;inset:0}
.abs{position:absolute}
.brand{top:40px;display:flex;align-items:center;gap:10px;color:var(--title-blue);font-weight:700;font-size:22px;line-height:1;white-space:nowrap}
.brand__mark{width:22px;height:22px;border-radius:50%;background:var(--red);flex:none}
.brand--collegium{left:225px}
.brand--engineering{left:580px}
.title{left:0;width:100%;text-align:center;font-family:"Anton",Impact,sans-serif;line-height:1;letter-spacing:.5px}
.title--top{top:100px;font-size:74px;color:var(--title-blue)}
.title--bottom{top:192px;font-size:74px;color:var(--red)}
.info{color:var(--white)}
.info__row{left:86px;display:flex;gap:22px;font-size:46px;line-height:1.02}
.info__row svg{flex:none;margin-top:6px}
.info__row--date{top:298px}
.info__row--place{top:366px;width:870px}
.host{left:66px;top:474px;width:900px;font-size:18.5px;line-height:1.28;color:var(--white);text-align:justify}
.host b{font-weight:700}
.section-head{left:0;top:596px;width:100%;display:flex;justify-content:center;align-items:center;gap:22px;color:var(--white);font-size:37px;font-weight:700}
.section-head::before,.section-head::after{content:"";width:118px;height:3px;background:var(--white)}
.portrait{
  position:absolute;border-radius:50%;border:6px solid var(--white);
  background:radial-gradient(circle at 50% 40%,var(--photo-a) 0 45%,var(--photo-b) 100%);
  box-shadow:-9px -9px 0 var(--red);
}
.keynote__name{font-size:23px;font-weight:700;color:var(--white);line-height:1.2}
.keynote__bio{margin-top:10px;font-size:15.5px;line-height:1.27;color:var(--white)}
.keynote--one{left:235px;top:706px;width:320px}
.keynote--two{left:762px;top:706px;width:240px}
.speaker-name{position:absolute;width:200px;text-align:center;font-size:23px;font-weight:700;color:var(--white)}
</style>
</head>
<body>
<article class="flyer">
  <svg class="flyer__bg" width="1013" height="1388" viewBox="0 0 1013 1388" aria-hidden="true">
    <defs>
      <linearGradient id="blueband" x1="0" x2="1" y1="0" y2="0">
        <stop offset="0" stop-color="#0f3474"/>
        <stop offset=".5" stop-color="#1b4f98"/>
        <stop offset="1" stop-color="#0f3474"/>
      </linearGradient>
    </defs>
    <rect width="1013" height="1388" fill="#ffffff"/>
    <path d="M0,243 Q506,335 1013,250 L1013,1388 L0,1388 Z" fill="#d12836"/>
    <path d="M0,690 Q506,380 1013,690 L1013,1388 L0,1388 Z" fill="url(#blueband)"/>
    <path d="M0,684 Q506,374 1013,684" fill="none" stroke="#ffffff" stroke-width="7"/>
    <rect y="1346" width="1013" height="6" fill="#ffffff"/>
    <rect y="1352" width="1013" height="36" fill="#d12836"/>
  </svg>

  <div class="brand brand--collegium abs"><span class="brand__mark"></span>Genomic Regulation Collegium</div>
  <div class="brand brand--engineering abs"><span class="brand__mark"></span>Halvorsen Engineering</div>

  <h1>
    <span class="title title--top abs">STIRRING AND SETTLING</span>
    <span class="title title--bottom abs">THE CHROMATIN MAP</span>
  </h1>

  <div class="info__row info__row--date info abs">
    <svg width="38" height="38" viewBox="0 0 38 38" aria-hidden="true"><rect x="3" y="7" width="32" height="28" rx="4" fill="none" stroke="#fff" stroke-width="3"/><line x1="3" y1="15" x2="35" y2="15" stroke="#fff" stroke-width="3"/><line x1="11" y1="3" x2="11" y2="10" stroke="#fff" stroke-width="3"/><line x1="27" y1="3" x2="27" y2="10" stroke="#fff" stroke-width="3"/></svg>
    <span>February 7th, 2019 &nbsp;( Thursday )</span>
  </div>
  <div class="info__row info__row--place info abs">
    <svg width="38" height="42" viewBox="0 0 38 42" aria-hidden="true"><path d="M19 2C10 2 4 9 4 17c0 10 15 23 15 23s15-13 15-23C34 9 28 2 19 2z" fill="#fff"/><circle cx="19" cy="17" r="6" fill="#d12836"/></svg>
    <span>Halvorsen College Dunmere School of Medicine</span>
  </div>
  <p class="host abs">It is being held by the <b>Genomic Regulation Collegium at the Vantreck Hall for Applied Discovery</b> (Kellaway Auditorium and Lobby, 2750 Orchard Terrace Way, Philadelphia, PA 19187)</p>

  <h2 class="section-head abs">Key Note Speakers</h2>

  <div class="portrait" style="left:48px;top:668px;width:176px;height:210px" role="img" aria-label="Portrait photo of Ottokar Brummell"></div>
  <div class="keynote--one abs">
    <h3 class="keynote__name">Ottokar Brummell, M.D</h3>
    <p class="keynote__bio">Professor of Biology at the Northvale Polytechnic of Applied Science; Founding Member of the Corriveau Foundation for Life Science Study; Member of the Council of Clinical Scholars.</p>
  </div>

  <div class="portrait" style="left:574px;top:662px;width:176px;height:206px" role="img" aria-label="Portrait photo of Thomas Weylund"></div>
  <div class="keynote--two abs">
    <h3 class="keynote__name">Thomas (Tom) Weylund, M.D.</h3>
    <p class="keynote__bio">President of the Lumavex Centers for Therapeutic Discovery (LCTD)</p>
  </div>

  <div class="portrait" style="left:56px;top:908px;width:156px;height:176px" role="img" aria-label="Speaker portrait photo"></div>
  <div class="portrait" style="left:302px;top:906px;width:156px;height:176px" role="img" aria-label="Speaker portrait photo"></div>
  <div class="portrait" style="left:552px;top:906px;width:156px;height:176px" role="img" aria-label="Speaker portrait photo"></div>
  <div class="portrait" style="left:774px;top:904px;width:156px;height:176px" role="img" aria-label="Speaker portrait photo"></div>
  <span class="speaker-name" style="left:40px;top:1088px">Lorem Ipsum</span>
  <span class="speaker-name" style="left:286px;top:1087px">Lorem Ipsum</span>
  <span class="speaker-name" style="left:532px;top:1087px">Lorem Ipsum</span>
  <span class="speaker-name" style="left:747px;top:1087px">Lorem Ipsum</span>

  <div class="portrait" style="left:80px;top:1138px;width:156px;height:174px" role="img" aria-label="Speaker portrait photo"></div>
  <div class="portrait" style="left:320px;top:1134px;width:156px;height:176px" role="img" aria-label="Speaker portrait photo"></div>
  <div class="portrait" style="left:554px;top:1136px;width:156px;height:174px" role="img" aria-label="Speaker portrait photo"></div>
  <div class="portrait" style="left:796px;top:1134px;width:156px;height:176px" role="img" aria-label="Speaker portrait photo"></div>
  <span class="speaker-name" style="left:55px;top:1316px">Lorem Ipsum</span>
  <span class="speaker-name" style="left:298px;top:1316px">Lorem Ipsum</span>
  <span class="speaker-name" style="left:531px;top:1313px">Lorem Ipsum</span>
  <span class="speaker-name" style="left:767px;top:1314px">Lorem Ipsum</span>
</article>
</body>
</html>
```